Auto Mechanic business card

Need a general business card for Kestrelworks.
Name on card should be 'Tidewell Garage'
Tel # (869) 555 0142
Address is - Palm Lane, Basseterre, St. Kitts
Whatsapp and facebook symbols should be added
On back of card should include services offered
General Repairs
Brakes
Tune Ups
Suspensions
Oil Leaks
Dent repairs
Suspensions
Car Sales
Tyre Repairs
General service
Check Engine Light
Minor Electricals

Target Market(s)

General Population, University students

Industry/Entity Type

Auto Mechanic

Contact Information for Business Card

Tidewell Garage

Requirements
Must have
• 2 Sides

```html
<!DOCTYPE html>
<html lang="en">
<head>
<meta charset="utf-8">
<title>Tidewell Garage – Business Card</title>
<link href="https://fonts.googleapis.com/css2?family=Roboto:wght@400;500&family=Roboto+Condensed:wght@400;700&display=swap" rel="stylesheet">
<style>
  :root {
    --backdrop: #1c1c1e;
    --card-red: #a3161c;
    --card-red-dark: #7d0f14;
    --card-black: #1f1f21;
    --card-black-light: #2b2b2e;
    --accent-red: #c4161c;
    --white: #ffffff;
    --silver: #e6e6e6;
  }
  * { box-sizing: border-box; margin: 0; padding: 0; }
  html, body { width: 1200px; height: 874px; overflow: hidden; }
  body {
    background: var(--backdrop);
    font-family: "Roboto", Arial, sans-serif;
    position: relative;
  }
  .card {
    position: absolute;
    left: 240px;
    width: 720px;
    height: 400px;
    border-radius: 22px;
    overflow: hidden;
    box-shadow: 0 12px 30px rgba(0,0,0,.55);
  }

  /* Services side */
  .card-services {
    top: 25px;
    background: radial-gradient(ellipse at 50% 40%, var(--card-red) 0%, var(--card-red-dark) 100%);
    color: var(--white);
  }
  .service-list {
    position: absolute;
    list-style: none;
    font-size: 21px;
    line-height: 27px;
  }
  .service-list li { display: flex; align-items: center; gap: 12px; }
  .service-list--left { left: 60px; top: 48px; }
  .service-list--right { right: 60px; top: 168px; }
  .service-list--right li { justify-content: flex-end; }
  .tick { width: 17px; height: 17px; flex: none; }

  /* Contact side */
  .card-contact {
    top: 449px;
    background: linear-gradient(160deg, var(--card-black-light), var(--card-black));
    color: var(--white);
  }
  .edge-tab {
    position: absolute; left: 0; top: 40px;
    width: 14px; height: 62px;
    background: var(--accent-red);
    border-radius: 0 8px 8px 0;
  }
  .phone {
    position: absolute; left: 52px; top: 34px;
    font-family: "Roboto Condensed", Arial, sans-serif;
    font-weight: 700; font-size: 56px; letter-spacing: .5px;
  }
  .address {
    position: absolute; left: 52px; top: 104px;
    font-family: "Roboto Condensed", Arial, sans-serif;
    font-size: 26px;
  }
  .social {
    position: absolute; left: 52px; top: 150px;
    display: flex; gap: 10px;
  }
  .social-dot {
    width: 40px; height: 40px; border-radius: 50%;
    background: var(--accent-red);
  }
  .brand-name {
    position: absolute; right: 80px; bottom: 92px;
    font-family: "Roboto Condensed", Arial, sans-serif;
    font-weight: 700; font-size: 58px; letter-spacing: 3px;
    text-transform: uppercase;
    color: var(--white);
  }
  .base-band {
    position: absolute; left: 0; bottom: 0;
    width: 100%; height: 56px;
    display: flex;
  }
  .base-band__red { flex: 0 0 68%; background: var(--accent-red); clip-path: polygon(0 0, 100% 0, 96% 100%, 0 100%); }
  .base-band__white { flex: 1; background: var(--silver); margin-left: -2.5%; clip-path: polygon(8% 0, 100% 0, 100% 100%, 0 100%); }
</style>
</head>
<body>
  <svg width="0" height="0" style="position:absolute">
    <symbol id="tick-icon" viewBox="0 0 20 20">
      <circle cx="10" cy="10" r="10" fill="#ffffff"/>
      <path d="M5.5 10.5 L8.6 13.4 L14.5 6.8" fill="none" stroke="#a3161c" stroke-width="2.4" stroke-linecap="round" stroke-linejoin="round"/>
    </symbol>
  </svg>

  <section class="card card-services" aria-label="Services offered">
    <ul class="service-list service-list--left">
      <li><svg class="tick"><use href="#tick-icon"/></svg>General Repairs</li>
      <li><svg class="tick"><use href="#tick-icon"/></svg>Brakes</li>
      <li><svg class="tick"><use href="#tick-icon"/></svg>Tune Ups</li>
      <li><svg class="tick"><use href="#tick-icon"/></svg>Suspensions</li>
      <li><svg class="tick"><use href="#tick-icon"/></svg>Oil Leaks</li>
      <li><svg class="tick"><use href="#tick-icon"/></svg>Dent Repairs</li>
    </ul>
    <ul class="service-list service-list--right">
      <li>Suspensions<svg class="tick"><use href="#tick-icon"/></svg></li>
      <li>Car Sales<svg class="tick"><use href="#tick-icon"/></svg></li>
      <li>Tyre Repairs<svg class="tick"><use href="#tick-icon"/></svg></li>
      <li>General Service<svg class="tick"><use href="#tick-icon"/></svg></li>
      <li>Check Engine Light<svg class="tick"><use href="#tick-icon"/></svg></li>
      <li>Minor Electricals<svg class="tick"><use href="#tick-icon"/></svg></li>
    </ul>
  </section>

  <section class="card card-contact" aria-label="Contact details">
    <div class="edge-tab"></div>
    <p class="phone">(869) 555 0142</p>
    <p class="address">Palm Lane, Basseterre, St. Kitts</p>
    <div class="social" aria-label="Messaging and social pages">
      <span class="social-dot"></span>
      <span class="social-dot"></span>
    </div>
    <p class="brand-name">Tidewell Garage</p>
    <div class="base-band">
      <span class="base-band__red"></span>
      <span class="base-band__white"></span>
    </div>
  </section>
</body>
</html>
```